Business Card Design

My business is writing crime novels to entertain readers. I write legal thrillers and mysteries. I need a card for publishers, agents, other authors, and media.

Industry/Entity Type

Legal

Contact Information for Business Card

Paul Trenholt
www.trenholtnoir.example
pbtrenholt@mailbox.example
0064 27 5170942

```html
<!DOCTYPE html>
<html lang="en">
<head>
<meta charset="utf-8">
<title>Paul Trenholt — Business Card</title>
<link rel="stylesheet" href="https://fonts.googleapis.com/css2?family=Cinzel:wght@700&family=Exo+2:wght@400;500&display=swap">
<style>
  :root {
    --card-white: #ffffff;
    --brand-red: #93272a;
    --brand-red-dark: #6e1c1f;
    --brand-red-light: #b52a2f;
    --text-red: #8e2a2c;
    --text-grey: #8a8a8c;
    --photo-grey-light: #9a9a9a;
    --photo-grey-dark: #6f6f6f;
  }
  * { margin: 0; padding: 0; box-sizing: border-box; }
  html, body { width: 1200px; height: 740px; overflow: hidden; background: var(--card-white); }
  .card { position: relative; width: 1200px; height: 740px; background: var(--card-white); font-family: "Exo 2", sans-serif; }

  .portrait {
    position: absolute; left: 95px; top: 127px; width: 342px; height: 440px;
    border-radius: 32px;
    background: radial-gradient(ellipse at 50% 35%, var(--photo-grey-light), var(--photo-grey-dark));
  }

  .name-band {
    position: absolute; left: 543px; top: 138px; width: 657px; height: 97px;
    background: var(--brand-red);
    display: flex; align-items: center; justify-content: center; padding-right: 30px;
  }
  .name {
    font-family: "Cinzel", serif; font-weight: 700; color: var(--card-white);
    font-size: 70px; letter-spacing: 1px; line-height: 1; white-space: nowrap;
  }

  .tagline {
    position: absolute; left: 560px; width: 612px; top: 280px;
    text-align: center; color: var(--text-red);
    font-size: 31px; letter-spacing: 3px; line-height: 46px; font-weight: 400;
  }

  .contacts { position: absolute; left: 560px; top: 434px; list-style: none; }
  .contact { display: flex; align-items: center; height: 42px; color: var(--text-grey); font-size: 29px; letter-spacing: 0.5px; }
  .contact-icon { width: 36px; height: 36px; margin-right: 18px; flex: none; }

  .footer { position: absolute; left: 0; top: 640px; width: 1200px; height: 100px; }
  .website {
    position: absolute; right: 62px; top: 676px;
    color: var(--card-white); font-size: 28px; letter-spacing: 3px; font-weight: 500;
  }
</style>
</head>
<body>
<div class="card">
  <div class="portrait" role="img" aria-label="Portrait photograph of the author"></div>

  <div class="name-band"><h1 class="name">Paul Trenholt</h1></div>

  <p class="tagline">LEGAL THRILLERS<br>AND MYSTERIES WRITING</p>

  <ul class="contacts">
    <li class="contact">
      <svg class="contact-icon" viewBox="0 0 36 36" aria-hidden="true">
        <rect x="9" y="2" width="16" height="32" rx="3" fill="var(--brand-red)"/>
        <rect x="12" y="6" width="10" height="9" fill="#fff"/>
        <g fill="#fff"><circle cx="13" cy="20" r="1.3"/><circle cx="17" cy="20" r="1.3"/><circle cx="21" cy="20" r="1.3"/><circle cx="13" cy="24" r="1.3"/><circle cx="17" cy="24" r="1.3"/><circle cx="21" cy="24" r="1.3"/><circle cx="13" cy="28" r="1.3"/><circle cx="17" cy="28" r="1.3"/><circle cx="21" cy="28" r="1.3"/></g>
      </svg>
      0064 27 5170942
    </li>
    <li class="contact">
      <svg class="contact-icon" viewBox="0 0 36 36" aria-hidden="true">
        <rect x="1" y="9" width="34" height="20" fill="var(--brand-red)"/>
        <path d="M2 10 L18 22 L34 10 M2 28 L14 19 M34 28 L22 19" stroke="#fff" stroke-width="1.6" fill="none"/>
      </svg>
      pbtrenholt@mailbox.example
    </li>
    <li class="contact">
      <svg class="contact-icon" viewBox="0 0 36 36" aria-hidden="true">
        <rect x="5" y="5" width="26" height="26" fill="var(--brand-red)"/>
      </svg>
      social.example/PaulTrenholtAuthor
    </li>
  </ul>

  <svg class="footer" viewBox="0 0 1200 100" aria-hidden="true">
    <defs>
      <linearGradient id="greyBand" x1="0" x2="1">
        <stop offset="0" stop-color="#000"/><stop offset="1" stop-color="#8a8a8c"/>
      </linearGradient>
      <linearGradient id="redStrip" x1="0" x2="1">
        <stop offset="0" stop-color="var(--brand-red-light)"/><stop offset="1" stop-color="var(--brand-red)"/>
      </linearGradient>
      <linearGradient id="redBlock" x1="0" x2="1">
        <stop offset="0" stop-color="var(--brand-red)"/><stop offset="1" stop-color="var(--brand-red-dark)"/>
      </linearGradient>
    </defs>
    <polygon points="0,23 662,23 640,62 0,62" fill="url(#greyBand)"/>
    <rect x="0" y="72" width="1200" height="28" fill="url(#redStrip)"/>
    <polygon points="690,9 1200,9 1200,100 636,100" fill="url(#redBlock)"/>
  </svg>
  <p class="website">www.trenholtnoir.example</p>
</div>
</body>
</html>
```